Geschäftspapiere für Motorboot-Verleih auf Trailern
Zielgruppe
MotorBoot Verleih auf Trailern
Aufgabenstellung
unsere Charterverträge, rechnungen etc. werden per email verschickt, bitte es als pdf konfigurieren, sodass ich es überall einsetzen kann, unsere homepage ist korvelmark.de

```html
<!DOCTYPE html>
<html lang="de">
<head>
<meta charset="utf-8">
<title>Korvelmark Geschäftspapiere</title>
<link href="https://fonts.googleapis.com/css2?family=Open+Sans:wght@400;600&display=swap" rel="stylesheet">
<style>
  :root {
    --navy: #0059a3;
    --cyan: #00d2f0;
    --paper: #ffffff;
    --stage: #ececec;
    --ink: #1e1e1e;
    --ghost: #f4f4f4;
    --fold: #c9c9c9;
  }
  * { box-sizing: border-box; margin: 0; padding: 0; }
  html, body { width: 1200px; height: 815px; overflow: hidden; }
  body { background: var(--stage); font-family: "Open Sans", Arial, sans-serif; position: relative; }

  .sheet { position: absolute; width: 490px; height: 693px; background: var(--paper); overflow: hidden; }
  .sheet--first { left: 80px; top: 64px; }
  .sheet--follow { left: 636px; top: 68px; }

  .head-band { position: absolute; left: 0; top: 13px; width: 100%; height: 51px; background: var(--navy); }
  .head-band::after { content: ""; position: absolute; right: 0; top: 0; width: 33px; height: 100%; background: var(--cyan); }

  .brand-badge {
    position: absolute; left: 380px; top: 11px; width: 88px; height: 88px; border-radius: 50%;
    background: var(--paper); border: 3px solid var(--navy);
    display: flex; align-items: center; justify-content: center;
    color: var(--navy); font-weight: 600; font-size: 12px; letter-spacing: .3px;
  }

  .sender-line {
    position: absolute; left: 57px; top: 121px; font-size: 5px; color: var(--ink);
    border-bottom: .5px solid var(--ink); padding-bottom: .5px; white-space: nowrap;
  }

  .contact-block {
    position: absolute; left: 385px; top: 123px; padding-left: 8px;
    border-left: 1px solid var(--ink); font-size: 6.6px; line-height: 9.1px; color: var(--ink);
  }
  .contact-block .address { margin-bottom: 3px; }
  .contact-row { display: flex; align-items: center; gap: 5px; }
  .contact-row svg { width: 6px; height: 6px; fill: var(--navy); }

  .fold-mark { position: absolute; left: 0; width: 14px; height: 0; border-top: .6px solid var(--fold); }
  .fold-mark--1 { top: 246px; }
  .fold-mark--2 { top: 346px; }
  .fold-mark--3 { top: 490px; }

  .backdrop-mark {
    position: absolute; left: 70px; top: 251px; width: 350px; height: 350px; border-radius: 50%;
    border: 11px solid var(--ghost); background: #fafafa;
    display: flex; align-items: center; justify-content: center;
    color: var(--ghost); font-size: 44px; font-weight: 600; letter-spacing: 2px;
  }

  .foot-band {
    position: absolute; left: 0; top: 656px; width: 100%; height: 23px; background: var(--navy);
    color: #fff; font-size: 6.4px; line-height: 8.6px;
  }
  .foot-band::after { content: ""; position: absolute; right: 0; top: 0; width: 26px; height: 100%; background: var(--cyan); }
  .foot-col { position: absolute; top: 3px; }
  .foot-col--bank { left: 31px; top: 4px; }
  .foot-col--register { left: 139px; top: 2px; }
  .foot-col--iban { left: 286px; top: 2px; }
  .foot-divider { position: absolute; top: 2px; height: 19px; border-left: .7px solid #fff; }
  .foot-divider--1 { left: 124px; }
  .foot-divider--2 { left: 271px; }

  .brand-badge--small {
    position: absolute; left: 424px; top: 648px; width: 42px; height: 42px; border-radius: 50%;
    background: var(--paper); border: 2px solid var(--navy);
    display: flex; align-items: center; justify-content: center;
    color: var(--navy); font-weight: 600; font-size: 6px;
  }
</style>
</head>
<body>

<section class="sheet sheet--first" aria-label="Briefbogen erste Seite">
  <div class="head-band"></div>
  <div class="brand-badge">Korvelmark</div>

  <div class="sender-line">Korvelmark GmbH | Lindenpfad 12 | 85277 Hohenwart</div>

  <address class="contact-block" style="font-style:normal">
    <div class="address">Korvelmark GmbH<br>Lindenpfad 12<br>85277 Hohenwart</div>
    <div class="contact-row"><svg viewBox="0 0 10 10"><path d="M2 1l2 2-1 1.5c.8 1.5 1.5 2.2 3 3L7.5 6l2 2-1.5 1.5C4.5 9 1 5.5.5 2.5z"/></svg>08441/318 4471</div>
    <div class="contact-row"><svg viewBox="0 0 10 10"><rect x="2.5" y="0.5" width="5" height="3"/><rect x="0.5" y="3.5" width="9" height="4" rx="1"/><rect x="2.5" y="7" width="5" height="2.5"/></svg>08441/318 4400</div>
    <div class="contact-row"><svg viewBox="0 0 10 10"><path d="M0 2h10v6H0z M0 2l5 3.5L10 2" stroke="#fff" stroke-width=".8"/></svg>info@korvelmark.de</div>
    <div class="contact-row"><svg viewBox="0 0 10 10"><circle cx="5" cy="5" r="4.6"/></svg>www.korvelmark.de</div>
  </address>

  <span class="fold-mark fold-mark--1"></span>
  <span class="fold-mark fold-mark--2"></span>
  <span class="fold-mark fold-mark--3"></span>

  <div class="backdrop-mark">KORVELMARK</div>

  <footer class="foot-band">
    <div class="foot-col foot-col--bank">Bankverbindung:<br>Bank: Uferbank Ilmtal eG</div>
    <span class="foot-divider foot-divider--1"></span>
    <div class="foot-col foot-col--register">Handelsregister: HRB 4172<br>Registergericht: Amtsgericht Ilmstadt</div>
    <span class="foot-divider foot-divider--2"></span>
    <div class="foot-col foot-col--iban">BIC: UFERDEM1XXX<br>IBAN: DE41 7105 0033 0042 8816 27</div>
  </footer>
  <div class="brand-badge--small">Korvelmark</div>
</section>

<section class="sheet sheet--follow" aria-label="Briefbogen Folgeseite">
  <div class="head-band"></div>
  <div class="brand-badge">Korvelmark</div>

  <span class="fold-mark fold-mark--1"></span>
  <span class="fold-mark fold-mark--2"></span>
  <span class="fold-mark fold-mark--3"></span>

  <div class="backdrop-mark">KORVELMARK</div>

  <footer class="foot-band">
    <div class="foot-col foot-col--bank">Bankverbindung:<br>Bank: Uferbank Ilmtal eG</div>
    <span class="foot-divider foot-divider--1"></span>
    <div class="foot-col foot-col--register">Handelsregister: HRB 4172<br>Registergericht: Amtsgericht Ilmstadt</div>
    <span class="foot-divider foot-divider--2"></span>
    <div class="foot-col foot-col--iban">BIC: UFERDEM1XXX<br>IBAN: DE41 7105 0033 0042 8816 27</div>
  </footer>
  <div class="brand-badge--small">Korvelmark</div>
</section>

</body>
</html>
```